VeloRoot Sample Packaging Design

We need a design - with assistance on logo and colours - of a box containing sample sachets of a new natural sports supplement for endurance athletes.
We have an idea of logo and colours but would like input, ideas and assistance to create a cool new brand.

The product is based on natural beetroot powder which is scientifically backed to improve sports performance.
We like clean minimal branding that looks scientific - such as Kestrel Fuel, Stack Grains, Cortex Well Max and TuL Omni Drive sachets.

Attached is the type of package we will be using with matt black sachets, so clean white with potentially a beetroot colour (hex 691a40??) and grey (a3b2c2??) but we would like your professional and creative input.

I have attached a rough logo mock up of the logo I designed, happy for you to develop this by making it a bit cleaner (left edges angled or curved maybe- change font also maybe??) or your own ideas if clean, simple and effective. I based mine off the Far Meridian logo and PB works well with VeloRoot and Personal Best.

The final design should be clean, minimalist, high end sports supplement with a science and natural beetroot feel.
Box size: 300mm x 130mm x 14mm

Target Market(s)

Elite athletes and professionals wanting natural and science-backed supplements that work. Probably mainly men.
The customers are long distance sportspeople and NOT bodybuilders! Including triathletes, cyclists, long distance runners and swimmers.
The brand must also appeal to club level athletes and weekend warriors (but this should be easy if it's targeted at elite level first)

Industry/Entity Type

Supplement

Font styles to use
Sans Serif

Colors

Designer to choose colors to be used in the design.

Requirements
Must have
• - New logo (I like the Far Meridian logo but open to new ideas!)
• - Clean, scientific look with a twist of "I'm natural and not full of sports supplement junk!!"
• - A shade of beetroot red/purple as the signature colour, without looking too feminine.
• - Our slogan is "Beat your best"
Should not have
• A bodybuilder look.

```html
<!DOCTYPE html>
<html lang="en">
<head>
<meta charset="utf-8">
<title>VeloRoot Sample Packaging</title>
<link rel="stylesheet" href="https://fonts.googleapis.com/css2?family=Exo+2:wght@500;600;700&family=Roboto+Condensed:wght@400;700&display=swap">
<style>
  :root {
    --backdrop: #e3e4e6;
    --panel-grey: #cfcfcf;
    --matt-black: #0b0b0c;
    --beet: #c2305c;
    --beet-deep: #8e1f45;
    --white: #ffffff;
    --ink: #2d2d2d;
    --ink-soft: #555555;
  }
  * { margin: 0; padding: 0; box-sizing: border-box; }
  html, body { width: 1200px; height: 656px; overflow: hidden; }
  body {
    background: var(--backdrop);
    position: relative;
    font-family: "Roboto Condensed", Arial, sans-serif;
  }

  /* Box front panel */
  .box-front {
    position: absolute;
    left: 50px; top: 190px;
    width: 660px; height: 287px;
    background: var(--matt-black);
    overflow: hidden;
  }
  .box-front .pattern-area {
    position: absolute;
    right: 0; top: 0;
    width: 235px; height: 100%;
    background: linear-gradient(90deg, rgba(11,11,12,1) 0%, #1e1e20 45%, #2c2c2f 100%);
  }
  .brand {
    display: flex; align-items: center; gap: 10px;
    font-family: "Exo 2", Arial, sans-serif;
    font-weight: 700;
    color: var(--white);
    letter-spacing: 1px;
  }
  .brand .brand-dot {
    border-radius: 50%;
    border: 3px solid var(--white);
  }
  .box-front .brand {
    position: absolute; left: 72px; top: 70px;
    font-size: 27px;
  }
  .box-front .brand-dot { width: 34px; height: 34px; }
  .box-front .product-title {
    position: absolute; left: 66px; top: 128px;
    font-family: "Exo 2", Arial, sans-serif;
    font-weight: 600;
    font-size: 27px; line-height: 30px;
    color: var(--beet);
  }
  .box-front .claims {
    position: absolute; left: 72px; top: 198px;
    color: var(--white);
    font-size: 13px; line-height: 19px;
  }
  .box-front .claims .sub { font-size: 16px; }
  .box-front .pack-count {
    position: absolute; left: 74px; top: 258px;
    color: var(--white);
    font-size: 9px; font-weight: 700; letter-spacing: .5px;
  }

  /* Sachet presentation */
  .sachet-panel {
    position: absolute;
    left: 894px; top: 81px;
    width: 306px; height: 492px;
    background: var(--panel-grey);
  }
  .sachet {
    position: absolute;
    left: 52px; top: 69px;
    width: 214px; height: 352px;
    background: var(--white);
    overflow: hidden;
  }
  .sachet .black-top {
    position: absolute; inset: 0;
    width: 100%; height: 100%;
  }
  .sachet .brand {
    position: absolute; left: 0; right: 0; top: 58px;
    flex-direction: column; gap: 10px;
    font-size: 21px;
  }
  .sachet .brand-dot { width: 30px; height: 30px; }
  .sachet .product-title {
    position: absolute; right: 30px; top: 218px;
    text-align: right;
    font-family: "Exo 2", Arial, sans-serif;
    font-weight: 600;
    font-size: 18px; line-height: 23px;
    color: var(--beet);
  }
  .sachet .claims {
    position: absolute; left: 40px; top: 273px;
    font-size: 11px; line-height: 15px;
    color: var(--ink-soft);
  }
  .sachet .claims .lead { font-weight: 700; color: var(--ink); }
  .sachet .claims .sub { font-size: 12px; }
  .serving-badge {
    position: absolute; right: 22px; bottom: 20px;
    width: 34px; height: 34px; border-radius: 50%;
    background: var(--beet);
    color: var(--white);
    display: flex; flex-direction: column; align-items: center; justify-content: center;
    font-family: "Exo 2", Arial, sans-serif;
  }
  .serving-badge .num { font-size: 16px; font-weight: 700; line-height: 15px; }
  .serving-badge .label { font-size: 5px; letter-spacing: .5px; }
</style>
</head>
<body>

  <section class="box-front" aria-label="Sample box front panel">
    <div class="pattern-area" role="img" aria-label="Repeating line pattern of beetroots"></div>
    <div class="brand"><span class="brand-dot"></span>VELOROOT</div>
    <h1 class="product-title">Beetroot<br>Nitrate Supplement</h1>
    <p class="claims">&bull;HIGH PROTEIN &bull; HIGH FIBRE<br><span class="sub">23 VITAMINS &amp; MINERALS</span></p>
    <p class="pack-count">4 SACHETS</p>
  </section>

  <section class="sachet-panel" aria-label="Single serving sachet">
    <div class="sachet">
      <svg class="black-top" viewBox="0 0 214 352" preserveAspectRatio="none" aria-hidden="true">
        <polygon points="0,0 214,0 214,112 0,258" fill="#0b0b0c"/>
      </svg>
      <div class="brand"><span class="brand-dot"></span>VELOROOT</div>
      <h2 class="product-title">Beetroot Nitrate<br>Supplement</h2>
      <p class="claims"><span class="lead">&bull;HIGH PROTEIN&bull; HIGH FIBRE</span><br><span class="sub">23 VITAMINS &amp;<br>MINERALS</span></p>
      <div class="serving-badge"><span class="num">1</span><span class="label">SERVING</span></div>
    </div>
  </section>

</body>
</html>
```